TORVEK SOLAR leaflet

I am looking for a leaflet design to post to letter boxes to increase business.

I do not want to advertise pricing but sell based on the value we offer

What services we offer:
Solar Systems
Battery Storage
Black out protection
Electric Vehicle charging
Air conditioning
See our Business cards and other leaflet made for print by real estate agent to go in their booklet. I wish the theme to be similar

See also leaflet made as template by us.. not professional to go to print. But you have some inspiration..

Also uploaded some logos of products we use.

Thankyou

```html
<!DOCTYPE html>
<html lang="en">
<head>
<meta charset="utf-8">
<title>Torvek Solar leaflet</title>
<link rel="stylesheet" href="https://fonts.googleapis.com/css2?family=Oswald:wght@500;600&family=Montserrat:wght@600;700;800&display=swap">
<style>
  :root {
    --bg: #d3d6d1;
    --green: #1f8a3b;
    --green-dark: #17702f;
    --yellow: #f5c518;
    --black: #0b0b0b;
    --white: #ffffff;
    --red: #d9262e;
    --sky: #5f9fdc;
    --panel: #1f2a44;
    --roof: #5b5f66;
  }
  * { margin: 0; padding: 0; box-sizing: border-box; }
  html, body { width: 1200px; height: 800px; overflow: hidden; background: var(--bg); }
  .stage { position: relative; width: 1200px; height: 800px; }
  .leaflet-frame { position: absolute; left: 331px; top: 20px; width: 537px; height: 760px; overflow: hidden; box-shadow: 0 4px 14px rgba(0,0,0,.18); }
  .leaflet { position: absolute; left: 0; top: 0; width: 918px; height: 1300px; transform: scale(0.585); transform-origin: 0 0; background: var(--white); overflow: hidden; }

  .hero-photo { position: absolute; left: 0; top: 0; width: 918px; height: 1110px;
    background: linear-gradient(180deg, #8fc0ea 0%, var(--sky) 14%, #6f8f5a 24%, #3f5a3a 30%, var(--panel) 40%, #2d3d63 55%, var(--roof) 72%, #4a4e55 100%); }

  .brand-box { position: absolute; left: 492px; top: 0; width: 426px; height: 262px; background: var(--white);
    display: flex; flex-direction: column; align-items: center; justify-content: center; gap: 10px; }
  .brand-dot { width: 64px; height: 64px; border-radius: 50%; background: var(--yellow); margin-bottom: 6px; }
  .brand-name { font-family: 'Montserrat', sans-serif; font-weight: 700; color: var(--green); font-size: 44px; letter-spacing: 2px; line-height: 1; }
  .brand-sub { font-family: 'Montserrat', sans-serif; font-weight: 700; color: var(--green); font-size: 26px; letter-spacing: 1px; line-height: 1; }

  .panels { position: absolute; left: 0; top: 0; width: 918px; height: 1300px; }

  .photo-circle { position: absolute; border-radius: 50%; border: 7px solid var(--green); }
  .photo-ac { left: 577px; top: 425px; width: 190px; height: 190px; background: radial-gradient(circle at 45% 50%, #f3f1ea 0%, #d9d3c3 55%, #b8ab8d 100%); }
  .photo-ev { left: 332px; top: 663px; width: 188px; height: 188px; background: radial-gradient(circle at 55% 50%, #e9eef5 0%, #b9cde6 50%, #5d86c0 100%); }
  .photo-inverter { position: absolute; left: 330px; top: 932px; width: 150px; height: 215px; border-radius: 14px;
    background: linear-gradient(180deg, #f4f5f6 0%, #dcdfe2 70%, #8d9096 100%); }

  .headline { position: absolute; left: 30px; top: 585px; font-family: 'Oswald', sans-serif; font-weight: 500;
    color: var(--white); font-size: 86px; line-height: 90px; }

  .services { position: absolute; left: 545px; top: 648px; }
  .services-title { font-family: 'Oswald', sans-serif; font-weight: 600; color: var(--green-dark); font-size: 68px; line-height: 80px; margin-bottom: 8px; }
  .service-list { list-style: none; }
  .service-item { display: flex; align-items: flex-start; gap: 16px; font-family: 'Oswald', sans-serif; font-weight: 500;
    color: var(--white); font-size: 40px; line-height: 40px; margin-bottom: 14px; }
  .service-icon { width: 36px; height: 36px; flex: none; margin-top: 2px; }

  .partners { position: absolute; left: 36px; top: 1100px; width: 360px; font-family: 'Montserrat', sans-serif; }
  .partner-main { position: absolute; left: 0; top: 26px; color: var(--green); font-weight: 800; font-size: 44px; line-height: 1; }
  .partner-tagline { position: absolute; left: 2px; top: 82px; color: var(--green); font-weight: 600; font-size: 18px; white-space: nowrap; }
  .partner-red { position: absolute; color: var(--red); font-weight: 800; line-height: 1; }
  .partner-veltra { left: 0; top: 140px; font-size: 40px; }
  .partner-veltra-tag { position: absolute; left: 14px; top: 188px; color: var(--red); font-weight: 700; font-size: 11px; letter-spacing: 2px; }
  .partner-ostrel { left: 236px; top: 144px; font-size: 34px; display: flex; align-items: center; gap: 8px; }
  .partner-ostrel::before { content: ""; width: 18px; height: 18px; border-radius: 50%; background: var(--red); }

  .contact { position: absolute; right: 26px; top: 1112px; text-align: right; font-family: 'Montserrat', sans-serif; }
  .social { display: flex; justify-content: flex-end; gap: 26px; margin-right: 46px; margin-bottom: 14px; }
  .social-dot { width: 40px; height: 40px; border-radius: 50%; background: var(--yellow); }
  .phone { color: var(--white); font-weight: 800; font-size: 46px; line-height: 52px; letter-spacing: 1px; }
  .email { color: var(--white); font-weight: 600; font-size: 29px; line-height: 36px; }
  .web { color: var(--yellow); font-weight: 700; font-size: 29px; line-height: 36px; }
</style>
</head>
<body>
<div class="stage">
  <div class="leaflet-frame">
    <div class="leaflet">
      <div class="hero-photo" role="img" aria-label="Photo of solar panels on a corrugated roof with gum trees and blue sky"></div>

      <svg class="panels" viewBox="0 0 918 1300" aria-hidden="true">
        <defs>
          <linearGradient id="greenBlend" x1="0" y1="0" x2="1" y2="0" gradientUnits="objectBoundingBox">
            <stop offset="0" stop-color="#1f8a3b"/>
            <stop offset="0.62" stop-color="#1f8a3b"/>
            <stop offset="0.85" stop-color="#8fb42a"/>
            <stop offset="1" stop-color="#f5c518"/>
          </linearGradient>
        </defs>
        <path d="M420,1100 L420,780 C470,650 590,560 710,560 C800,560 880,610 918,660 L918,1100 Z" fill="#f5c518"/>
        <path d="M420,780 C470,650 590,560 710,560 C800,560 880,610 918,660" fill="none" stroke="#ffffff" stroke-width="24"/>
        <path d="M0,1100 L0,520 C110,460 270,470 360,570 C410,625 430,700 440,780 L440,1100 Z" fill="url(#greenBlend)"/>
        <path d="M0,520 C110,460 270,470 360,570 C410,625 430,700 440,780" fill="none" stroke="#ffffff" stroke-width="24"/>
        <rect x="0" y="1090" width="918" height="210" fill="#ffffff"/>
        <path d="M392,1300 C470,1170 620,1095 918,1088 L918,1300 Z" fill="#0b0b0b"/>
      </svg>

      <div class="brand-box">
        <div class="brand-dot"></div>
        <div class="brand-name">TORVEK SOLAR</div>
        <div class="brand-sub">+ ELECTRICAL</div>
      </div>

      <div class="photo-circle photo-ac" role="img" aria-label="Photo of an air conditioning outdoor unit"></div>
      <div class="photo-circle photo-ev" role="img" aria-label="Photo of an electric car being charged"></div>
      <div class="photo-inverter" role="img" aria-label="Photo of a solar inverter unit"></div>

      <h1 class="headline">Adelaide’s<br>leading<br>Solar and<br>Battery<br>provider</h1>

      <section class="services">
        <h2 class="services-title">Services</h2>
        <ul class="service-list">
          <li class="service-item">
            <svg class="service-icon" viewBox="0 0 36 36" fill="none" stroke="#17702f" stroke-width="2"><path d="M3 30 L8 14 H28 L33 30 Z M6 22 H30 M14 14 L12 30 M22 14 L24 30"/><circle cx="28" cy="6" r="3"/></svg>
            Solar Systems</li>
          <li class="service-item">
            <svg class="service-icon" viewBox="0 0 36 36" fill="none" stroke="#17702f" stroke-width="2"><rect x="4" y="10" width="28" height="20"/><path d="M9 10 V6 M27 10 V6 M19 14 L15 21 H21 L17 27"/></svg>
            Battery Storage</li>
          <li class="service-item">
            <svg class="service-icon" viewBox="0 0 36 36" fill="none" stroke="#17702f" stroke-width="2"><rect x="9" y="3" width="18" height="30" rx="3"/><circle cx="18" cy="22" r="4"/><path d="M14 9 H22"/></svg>
            Black out protection</li>
          <li class="service-item">
            <svg class="service-icon" viewBox="0 0 36 36" fill="none" stroke="#17702f" stroke-width="2"><rect x="5" y="4" width="16" height="28" rx="2"/><path d="M14 9 L10 16 H16 L12 23 M21 14 H27 V26 C27 30 32 30 32 26 V10"/></svg>
            <span>Electric Vehicle<br>Charging</span></li>
          <li class="service-item">
            <svg class="service-icon" viewBox="0 0 36 36" fill="none" stroke="#17702f" stroke-width="2"><rect x="3" y="8" width="30" height="14" rx="2"/><path d="M7 18 H29 M10 26 V31 M18 26 V31 M26 26 V31"/></svg>
            Air Conditioning</li>
        </ul>
      </section>

      <div class="partners">
        <div class="partner-main">Korrin Solar</div>
        <div class="partner-tagline">Panels you can rely on</div>
        <div class="partner-red partner-veltra">Veltra</div>
        <div class="partner-veltra-tag">POWER THAT LASTS</div>
        <div class="partner-red partner-ostrel">Ostrel</div>
      </div>

      <address class="contact" style="font-style: normal;">
        <div class="social"><span class="social-dot"></span><span class="social-dot"></span></div>
        <div class="phone">0400 555 017</div>
        <div class="email">info@torvekelectrical.com.au</div>
        <div class="web">www.torvekelectrical.com.au</div>
      </address>
    </div>
  </div>
</div>
</body>
</html>
```